Logo and packaging design for Lime restoration mortar

We need a logo and packaging design for out line of restoration profits. This includes labels for pales, and cement bags. I have attached out current logo. And a design from you that I really like. This is the kind of colour scheme and style I would like for our packaging.

I would like a new logo that is similar, or related to our existing but more presentable in a retail environment. I think a mark is also necessary for the logo. Currently it is just words and that makes branding a bit difficult.

Target Market(s)

DIYers we will be selling to hardware stores

Logo Text

Fernlow

Requirements
Must have
• Logo and packaging template that uses the new logo.
Nice to have
• I really like impactful logos. I love the crown logo, however I would prefer not to copy it. I would like a impactful logo, that can be easily broken down for branding different products.

```html
<!DOCTYPE html>
<html lang="en">
<head>
<meta charset="utf-8">
<title>Fernlow Group — Packaging Labels</title>
<link href="https://fonts.googleapis.com/css2?family=Raleway:wght@300;800;900&family=Oswald:wght@500&display=swap" rel="stylesheet">
<style>
  :root{
    --bg:#e9e9e9;
    --bag-white:#f1f1ef;
    --navy:#2c2466;
    --lime-blue:#0d68a5;
    --lime-accent:#8fcbe6;
    --cement-red:#b71c24;
    --cement-accent:#e3831f;
    --label-text:#f1f1ef;
  }
  *{box-sizing:border-box;margin:0;padding:0}
  html,body{width:1200px;height:1200px;overflow:hidden}
  body{
    background:var(--bg);
    font-family:"Raleway",sans-serif;
    display:flex;align-items:center;justify-content:center;gap:60px;
  }
  .pack{
    position:relative;
    width:26em;height:43em;
    background:var(--bag-white);
    border-radius:.7em;
    overflow:hidden;
    text-align:center;
  }
  .pack--lime{font-size:20px;--accent:var(--lime-blue);--highlight:var(--lime-accent)}
  .pack--cement{font-size:17px;--accent:var(--cement-red);--highlight:var(--cement-accent)}

  .brand{position:absolute;top:9em;left:0;right:0;color:var(--navy);font-weight:900;line-height:1}
  .brand__name{font-size:3.5em;letter-spacing:.01em}
  .brand__group{font-size:1.9em;margin-top:.25em}

  .band{
    position:absolute;left:0;right:0;bottom:0;height:22em;
    background:var(--accent);
    padding:2.2em 2.6em 0;
  }
  .product__type{color:var(--highlight);font-weight:900;font-size:4.2em;line-height:1}
  .product__line{color:var(--label-text);font-size:2.9em;line-height:1.1}
  .product__line--bold{font-weight:900;margin-top:.2em}
  .product__line--light{font-weight:300}

  .rule{border:0;border-top:2px solid var(--label-text);opacity:.85;margin:.9em 0 .7em}
  .features{display:flex;align-items:center;justify-content:space-between;color:var(--label-text)}
  .feature{display:flex;align-items:center;gap:.45em;font-size:.95em;line-height:1.1;text-align:left}
  .feature svg{width:1.8em;height:1.8em;stroke:var(--label-text);fill:none;stroke-width:1.4}
  .weight{color:var(--highlight);font-family:"Oswald",sans-serif;font-weight:500;font-size:2em}
  .weight small{font-family:"Raleway",sans-serif;font-size:.4em;color:var(--label-text);vertical-align:top;margin-left:.2em}
</style>
</head>
<body>
  <section class="pack pack--lime">
    <div class="brand">
      <div class="brand__name">FERNLOW</div>
      <div class="brand__group">GROUP</div>
    </div>
    <div class="band">
      <div class="product__type">LIME</div>
      <div class="product__line product__line--bold">RESTORATION</div>
      <div class="product__line product__line--light">MORTAR</div>
      <hr class="rule">
      <div class="features">
        <div class="feature">
          <svg viewBox="0 0 24 24"><circle cx="12" cy="10" r="7"/><path d="M8 16l-2 6 3-1.5L11 22M16 16l2 6-3-1.5L13 22"/></svg>
          <span>Premium<br>Quality</span>
        </div>
        <div class="feature">
          <svg viewBox="0 0 24 24"><path d="M3 11h4v10H3zM7 12l4-7c1.5 0 2 1 2 2l-1 4h6c1.2 0 2 1 1.8 2.2l-1.3 6c-.2 1-1 1.8-2 1.8H7"/></svg>
          <span>Easy to<br>Use</span>
        </div>
        <div class="weight">50<small>Kg</small></div>
      </div>
    </div>
  </section>

  <section class="pack pack--cement">
    <div class="brand">
      <div class="brand__name">FERNLOW</div>
      <div class="brand__group">GROUP</div>
    </div>
    <div class="band">
      <div class="product__type">CEMENT</div>
      <div class="product__line product__line--bold">GENERAL</div>
      <div class="product__line product__line--light">PURPOSE</div>
      <hr class="rule">
      <div class="features">
        <div class="feature">
          <svg viewBox="0 0 24 24"><circle cx="12" cy="10" r="7"/><path d="M8 16l-2 6 3-1.5L11 22M16 16l2 6-3-1.5L13 22"/></svg>
          <span>Premium<br>Quality</span>
        </div>
        <div class="feature">
          <svg viewBox="0 0 24 24"><path d="M3 11h4v10H3zM7 12l4-7c1.5 0 2 1 2 2l-1 4h6c1.2 0 2 1 1.8 2.2l-1.3 6c-.2 1-1 1.8-2 1.8H7"/></svg>
          <span>Easy to<br>Use</span>
        </div>
        <div class="weight">50<small>Kg</small></div>
      </div>
    </div>
  </section>
</body>
</html>
```